Update Financial Planning Presentation

We currently use a stock Powerpoint template. Information is imputed into an Excel spreadsheet and then linked to the presentation. We are looking to improve and upgrade this to a more straightforward and "cleaner" looking template. I have attached a sample copy of the Powerpoint presantation we currently use along with the Excel spreadsheet. I have attached our logo as well. Thanks.
Industry/Entity Type
Financial

```html
<!DOCTYPE html>
<html lang="en">
<head>
<meta charset="utf-8">
<title>Financial Review – Slide Deck Overview</title>
<link href="https://fonts.googleapis.com/css2?family=Open+Sans:wght@400;600;700&display=swap" rel="stylesheet">
<style>
:root{
  --canvas:#a5a9ae;
  --paper:#ffffff;
  --green:#6f9450;
  --green-dark:#4f7a2f;
  --green-mid:#8fb06f;
  --green-light:#cfdfbd;
  --green-pale:#e6efdb;
  --olive:#6c8857;
  --ink:#333333;
  --copy:#6d6d6d;
  --blue:#3b5ea8;
  --accent:#f29a38;
}
*{margin:0;padding:0;box-sizing:border-box}
html,body{width:1200px;height:605px;overflow:hidden;background:var(--canvas);font-family:'Open Sans',Arial,sans-serif}
.deck{position:relative;width:1200px;height:605px}
.slide{position:absolute;width:180px;height:102px;background:var(--paper);overflow:hidden;box-shadow:0 0 1px rgba(0,0,0,.35)}
.slide.is-selected{outline:2px solid var(--accent)}
.slide-num{position:absolute;font-size:8px;color:var(--ink)}
.title{position:absolute;left:6px;top:4px;font-size:6.6px;font-weight:600;color:var(--green-dark);white-space:nowrap}
.corner{position:absolute;right:4px;top:3px;width:11px;height:11px;background:var(--green)}
.rule{position:absolute;left:4px;right:18px;top:15.5px;height:.6px;background:var(--green)}
.foot-line{position:absolute;left:4px;right:4px;bottom:5px;height:.6px;background:var(--green)}
.brand{position:absolute;left:6px;bottom:7px;font-size:2.8px;font-weight:600;color:var(--green-dark);display:flex;align-items:center;gap:1px}
.brand i{display:inline-block;width:2.4px;height:2.4px;background:var(--ink);border-radius:50%}
.copy{position:absolute;font-size:2.5px;line-height:3.3px;color:var(--copy);overflow:hidden}
.sidebar-copy{color:var(--green-dark)}
.table{position:absolute;font-size:2.2px;line-height:3px;color:var(--ink);border-collapse:collapse}
.table td{padding:0 1px;border-bottom:.3px solid #ddd;white-space:nowrap}
.table .band td{background:var(--green-light)}
.table .head td{background:var(--green);color:#fff;font-weight:600}
.checks{position:absolute;list-style:none;font-size:3.4px;line-height:6.2px;color:var(--ink)}
.checks li::before{content:"";display:inline-block;width:2px;height:3px;margin-right:3px;border-right:.8px solid var(--green-mid);border-bottom:.8px solid var(--green-mid);transform:rotate(40deg)}
.divider-v{position:absolute;width:.5px;background:#bbb}
.photo{position:absolute;background:linear-gradient(120deg,#e9ecec 0%,#cfd5d6 45%,#8d9597 70%,#dfe3e3 100%)}
.box-head{position:absolute;background:var(--green);color:#fff;font-size:2.4px;text-align:center;line-height:4px}
.kicker{position:absolute;font-size:3px;font-weight:700;color:var(--ink);letter-spacing:.1px}
</style>
</head>
<body>
<main class="deck">

<!-- Row 1 -->
<section class="slide" style="left:8px;top:0">
  <div class="copy" style="left:6px;top:4px;width:40px;font-size:2px;line-height:2.8px">Overview<br>About Us<br>Lifecycle<br>Process<br>Personal Info<br>Balance Sheet<br>Goals<br>Expenses<br>Income<br>Life Expectancy<br>Timeline<br>Benefits<br>Pension<br>Investments<br>Inflation<br>Plan<br>Review</div>
  <div style="position:absolute;left:48px;top:2px;width:130px;height:68px;background:var(--olive)"></div>
  <div style="position:absolute;left:58px;top:10px;font-size:10px;color:#e2ecd5">Financial Review</div>
  <div style="position:absolute;right:6px;top:22px;font-size:2.6px;color:#e2ecd5">Prepared For</div>
  <div style="position:absolute;right:6px;top:31px;font-size:7.4px;font-weight:700;color:#fff">John &amp; Jane Doe</div>
  <div style="position:absolute;right:6px;top:41px;font-size:2.8px;color:#e2ecd5">July 12, 2013</div>
  <div style="position:absolute;left:86px;top:78px;font-size:5px;font-weight:600;color:var(--green-dark);display:flex;align-items:center;gap:2px"><span style="width:4px;height:4px;border-radius:50%;background:var(--ink)"></span>northfield financial</div>
</section>
<div class="slide-num" style="left:8px;top:106px">1</div>

<section class="slide is-selected" style="left:208px;top:0">
  <div class="photo" style="inset:0" role="img" aria-label="Photo of three business people walking and talking in a bright office corridor"></div>
</section>
<div class="slide-num" style="left:208px;top:106px">2</div>

<section class="slide" style="left:408px;top:0">
  <div class="title">About Us</div><div class="corner"></div><div class="rule"></div>
  <p class="copy" style="left:6px;top:19px;width:168px;height:60px">We are an independent planning firm serving families and business owners. Our advisors build clear plans around each client's goals, income and savings, and we review them together every year.<br><br>We guide clients through retirement, tax, insurance and estate questions with plain advice. Every plan is reviewed with care and updated as life changes.<br><br>Our team works as one office, sharing knowledge so each client gets steady support from first meeting through retirement and beyond.</p>
  <div class="foot-line"></div><div class="brand"><i></i>northfield financial</div>
</section>
<div class="slide-num" style="left:408px;top:106px">3</div>

<section class="slide" style="left:608px;top:0">
  <div class="title">Common Lifecycle Periods</div><div class="corner"></div><div class="rule"></div>
  <svg style="position:absolute;left:0;top:0" width="180" height="102" viewBox="0 0 180 102">
    <ellipse cx="90" cy="58" rx="56" ry="32" fill="var(--green-light)"/>
    <line x1="90" y1="26" x2="90" y2="46" stroke="#fff" stroke-width=".8"/>
    <line x1="55" y1="62" x2="36" y2="78" stroke="#fff" stroke-width=".8"/>
    <line x1="125" y1="62" x2="144" y2="78" stroke="#fff" stroke-width=".8"/>
    <ellipse cx="90" cy="58" rx="23" ry="12" fill="var(--green-mid)"/>
    <text x="90" y="60" font-size="4.6" fill="#fff" text-anchor="middle">Lifecycle Periods</text>
    <g font-size="3.4" fill="var(--ink)" text-anchor="middle">
      <text x="90" y="32">Retirement</text>
      <text x="60" y="46">Pre-Retirement</text>
      <text x="122" y="46">Early Career</text>
      <text x="66" y="76">Accumulation</text>
      <text x="116" y="76">Mid Career</text>
    </g>
    <g font-size="2" fill="var(--copy)" text-anchor="middle">
      <text x="90" y="36">(Age 65+)</text>
      <text x="60" y="50">(Age 55 - 65)</text>
      <text x="122" y="50">(Age 25 - 35)</text>
      <text x="66" y="80">(Age 35 - 45)</text>
      <text x="116" y="80">(Age 45 - 55)</text>
    </g>
  </svg>
  <div class="foot-line"></div><div class="brand"><i></i>northfield financial</div>
</section>
<div class="slide-num" style="left:608px;top:106px">4</div>

<section class="slide" style="left:808px;top:0">
  <div class="title">Financial Planning Process</div><div class="corner"></div>
  <svg style="position:absolute;left:0;top:0" width="180" height="102" viewBox="0 0 180 102">
    <polygon points="22,30 142,30 142,14 176,54 142,94 142,78 22,78" fill="var(--olive)"/>
    <g fill="var(--green-light)">
      <rect x="16" y="38" width="19" height="34"/><rect x="39" y="38" width="19" height="34"/>
      <rect x="62" y="38" width="19" height="34"/><rect x="85" y="38" width="19" height="34"/>
      <rect x="108" y="38" width="19" height="34"/><rect x="131" y="38" width="19" height="34"/>
    </g>
    <g font-size="2.6" fill="var(--ink)" text-anchor="middle">
      <text x="25.5" y="50">Clarify</text><text x="25.5" y="54">Present</text><text x="25.5" y="58">Situation</text>
      <text x="48.5" y="48">Identify</text><text x="48.5" y="52">Financial</text><text x="48.5" y="56">and</text><text x="48.5" y="60">Personal</text><text x="48.5" y="64">Goals</text>
      <text x="71.5" y="50">Identify</text><text x="71.5" y="54">Financial</text><text x="71.5" y="58">Problems</text>
      <text x="94.5" y="50">Create a</text><text x="94.5" y="54">Written</text><text x="94.5" y="58">Plan and</text><text x="94.5" y="62">Strategies</text>
      <text x="117.5" y="50">Implement</text><text x="117.5" y="54">Strategies</text><text x="117.5" y="58">and</text><text x="117.5" y="62">Solutions</text>
      <text x="140.5" y="50">Ongoing</text><text x="140.5" y="54">Review</text><text x="140.5" y="58">and</text><text x="140.5" y="62">Revision</text>
    </g>
  </svg>
  <div class="foot-line"></div><div class="brand"><i></i>northfield financial</div>
</section>
<div class="slide-num" style="left:808px;top:106px">5</div>

<section class="slide" style="left:1013px;top:0">
  <div class="title">Personal Information</div><div class="corner"></div><div class="rule"></div>
  <table class="table" style="left:20px;top:20px;width:140px">
    <tr class="head"><td>Client</td><td>Spouse</td><td>Status</td></tr>
    <tr><td>Name</td><td>John</td><td>Married</td></tr>
    <tr><td>Birth</td><td>Jane</td><td>Yes</td></tr>
    <tr><td>Age</td><td>64</td><td>61</td></tr>
    <tr><td>Health</td><td>Good</td><td>Good</td></tr>
    <tr><td>Smoker</td><td>No</td><td>No</td></tr>
    <tr><td>Employer</td><td>Retail</td><td>School</td></tr>
    <tr><td>Income</td><td>$48,000</td><td>$36,000</td></tr>
    <tr class="band"><td>Children</td><td>Age</td><td>Status</td></tr>
    <tr><td>Child one</td><td>34</td><td>Single</td></tr>
    <tr><td>Child two</td><td>31</td><td>Married</td></tr>
    <tr><td>Child three</td><td>27</td><td>Single</td></tr>
  </table>
  <div class="foot-line"></div><div class="brand"><i></i>northfield financial</div>
</section>
<div class="slide-num" style="left:1013px;top:106px">6</div>

<!-- Row 2 -->
<section class="slide" style="left:8px;top:126px">
  <div class="title">Balance Sheet</div><div class="corner"></div><div class="rule"></div>
  <p class="copy sidebar-copy" style="left:6px;top:20px;width:46px;height:42px">A summary of what you own and what you owe, showing your current net worth at a glance for planning.</p>
  <table class="table" style="left:58px;top:19px;width:100px">
    <tr class="head"><td>Assets</td><td>Client</td><td>Total</td></tr>
    <tr class="band"><td>Chequing</td><td>$4,000</td><td>$4,000</td></tr>
    <tr class="band"><td>Savings</td><td>$12,000</td><td>$12,000</td></tr>
    <tr class="band"><td>RRSP</td><td>$98,000</td><td>$98,000</td></tr>
    <tr class="band"><td>TFSA</td><td>$20,000</td><td>$20,000</td></tr>
    <tr class="band"><td>Home</td><td>$350,000</td><td>$350,000</td></tr>
    <tr><td>Total Assets</td><td></td><td>$484,000</td></tr>
    <tr class="band"><td>Mortgage</td><td>$90,000</td><td>$90,000</td></tr>
    <tr class="band"><td>Loan</td><td>$8,000</td><td>$8,000</td></tr>
    <tr><td>Total Debts</td><td></td><td>$98,000</td></tr>
    <tr class="band"><td>Net Worth</td><td></td><td>$386,000</td></tr>
  </table>
  <div class="foot-line"></div><div class="brand"><i></i>northfield financial</div>
</section>
<div class="slide-num" style="left:8px;top:232px">7</div>

<section class="slide" style="left:208px;top:126px">
  <div class="title">Goals and Objectives</div><div class="corner"></div><div class="rule"></div>
  <ul class="checks" style="left:30px;top:22px">
    <li>Jane to Retire at Age 68</li>
    <li>John to Retire at Age 62</li>
    <li>Monthly Income at Retirement of $7,000.00 *</li>
    <li>Maintain Current Lifestyle in Retirement</li>
    <li>Portfolio Management</li>
  </ul>
  <div class="foot-line"></div><div class="brand"><i></i>northfield financial</div>
</section>
<div class="slide-num" style="left:208px;top:232px">8</div>

<section class="slide" style="left:408px;top:126px">
  <div class="title">Lifestyle Expenses - Current</div><div class="corner"></div><div class="rule"></div>
  <p class="copy sidebar-copy" style="left:6px;top:20px;width:46px;height:42px">Your monthly spending today, grouped by category, forms the base for the retirement income target.</p>
  <table class="table" style="left:60px;top:19px;width:108px">
    <tr class="band"><td>Housing</td><td>$1,200</td></tr><tr class="band"><td>Utilities</td><td>$300</td></tr>
    <tr class="band"><td>Food</td><td>$800</td></tr><tr class="band"><td>Transport</td><td>$500</td></tr>
    <tr class="band"><td>Insurance</td><td>$250</td></tr><tr class="band"><td>Health</td><td>$150</td></tr>
    <tr class="band"><td>Travel</td><td>$400</td></tr><tr class="band"><td>Gifts</td><td>$100</td></tr>
    <tr class="band"><td>Clothing</td><td>$150</td></tr><tr class="band"><td>Hobbies</td><td>$200</td></tr>
    <tr class="band"><td>Other</td><td>$150</td></tr><tr class="band"><td>Total</td><td>$4,200</td></tr>
  </table>
  <div class="foot-line"></div><div class="brand"><i></i>northfield financial</div>
</section>
<div class="slide-num" style="left:408px;top:232px">9</div>

<section class="slide" style="left:608px;top:126px">
  <div class="title">Income &amp; Expenses - Current</div><div class="corner"></div><div class="rule"></div>
  <p class="copy sidebar-copy" style="left:6px;top:20px;width:46px;height:42px">Income from all sources compared with total spending shows how much can be saved each month.</p>
  <table class="table" style="left:60px;top:19px;width:100px">
    <tr class="band"><td>Income</td><td></td></tr><tr><td>Salary John</td><td>$4,000</td></tr>
    <tr><td>Salary Jane</td><td>$3,000</td></tr><tr><td>Total Income</td><td>$7,000</td></tr>
    <tr class="band"><td>Deductions</td><td></td></tr><tr><td>Tax</td><td>$1,600</td></tr>
    <tr><td>Pension</td><td>$400</td></tr><tr class="band"><td>Expenses</td><td></td></tr>
    <tr><td>Lifestyle</td><td>$4,200</td></tr><tr class="band"><td>Surplus</td><td></td></tr>
    <tr><td>Monthly</td><td>$800</td></tr><tr><td>Annual</td><td>$9,600</td></tr>
  </table>
  <div class="foot-line"></div><div class="brand"><i></i>northfield financial</div>
</section>
<div class="slide-num" style="left:608px;top:232px">10</div>

<section class="slide" style="left:808px;top:126px">
  <div class="title">Life Expectancy</div><div class="corner"></div><div class="rule"></div>
  <svg style="position:absolute;left:0;top:0" width="180" height="102" viewBox="0 0 180 102">
    <line x1="40" y1="86" x2="150" y2="86" stroke="#aaa" stroke-width=".4"/>
    <rect x="50" y="28" width="7" height="58" fill="var(--blue)"/><rect x="57" y="24" width="7" height="62" fill="var(--green-mid)"/>
    <rect x="86" y="50" width="7" height="36" fill="var(--blue)"/><rect x="93" y="46" width="7" height="40" fill="var(--green-mid)"/>
    <rect x="122" y="64" width="7" height="22" fill="var(--blue)"/><rect x="129" y="60" width="7" height="26" fill="var(--green-mid)"/>
    <g font-size="2.4" fill="var(--ink)" text-anchor="middle">
      <text x="57" y="90">Age 30</text><text x="93" y="90">Age 60</text><text x="129" y="90">Age 80</text>
    </g>
    <rect x="78" y="92" width="3" height="2" fill="var(--blue)"/><text x="83" y="94" font-size="2">Male</text>
    <rect x="96" y="92" width="3" height="2" fill="var(--green-mid)"/><text x="101" y="94" font-size="2">Female</text>
  </svg>
  <div class="brand"><i></i>northfield financial</div>
</section>
<div class="slide-num" style="left:808px;top:232px">11</div>

<section class="slide" style="left:1013px;top:126px">
  <div class="title">Timeline</div><div class="corner"></div><div class="rule"></div>
  <ul class="checks" style="left:56px;top:28px;line-height:8px;width:110px">
    <li>Current Age (Youngest)<span style="position:absolute;left:90px">64</span></li>
    <li>Retirement Age<span style="position:absolute;left:90px">68</span></li>
    <li>Life Expectancy<span style="position:absolute;left:90px">90</span></li>
    <li>Retirement Period<span style="position:absolute;left:90px">30</span></li>
  </ul>
  <div class="foot-line"></div><div class="brand"><i></i>northfield financial</div>
</section>
<div class="slide-num" style="left:1013px;top:232px">12</div>

<!-- Row 3 -->
<section class="slide" style="left:8px;top:252px">
  <div class="title">Government Benefits</div><div class="corner"></div><div class="rule"></div>
  <p class="copy sidebar-copy" style="left:6px;top:20px;width:46px;height:42px">Public pension and old age benefits you can expect, shown as monthly amounts in today's dollars.</p>
  <div class="copy" style="left:62px;top:20px;width:100px;color:var(--ink)">
    <b>Current Monthly Benefits</b><br>Maximum Old Age Security at 65 <span style="float:right">$546</span><br>Maximum Pension Plan at 65 <span style="float:right">$1,012</span><br><br>Pension Plan at Age 60<br>&nbsp;John at 64 <span style="float:right">$624</span><br>&nbsp;Jane at 65 <span style="float:right">$466</span><br><br>Total Benefits <span style="float:right">$2,102</span>
  </div>
  <div class="copy" style="left:62px;top:70px;width:100px;font-size:2px">* Amounts are indexed each year to inflation.</div>
  <div class="foot-line"></div><div class="brand"><i></i>northfield financial</div>
</section>
<div class="slide-num" style="left:8px;top:358px">13</div>

<section class="slide" style="left:208px;top:252px">
  <div class="title">Pension Projections</div><div class="corner"></div><div class="rule"></div>
  <p class="copy sidebar-copy" style="left:6px;top:20px;width:46px;height:42px">Projected workplace pension income at retirement, based on current service and salary estimates.</p>
  <div class="divider-v" style="left:56px;top:22px;height:70px"></div>
  <div class="foot-line"></div><div class="brand"><i></i>northfield financial</div>
</section>
<div class="slide-num" style="left:208px;top:358px">14</div>

<section class="slide" style="left:408px;top:252px">
  <div class="title">Investment Planning</div><div class="corner"></div><div class="rule"></div>
  <div class="copy" style="left:6px;top:20px;width:44px;color:var(--ink);font-weight:600">4% Rate<br><br>Investment Needs at Retirement<br><br>Capital Required to Fund Goal</div>
  <table class="table" style="left:58px;top:19px;width:112px">
    <tr class="head"><td>Year</td><td>Need</td><td>Capital</td></tr>
    <tr class="band"><td>2014</td><td>$7,000</td><td>$610,000</td></tr><tr><td>2015</td><td>$7,140</td><td>$622,000</td></tr>
    <tr class="band"><td>2016</td><td>$7,283</td><td>$634,000</td></tr><tr><td>2017</td><td>$7,428</td><td>$647,000</td></tr>
    <tr class="band"><td>2018</td><td>$7,577</td><td>$660,000</td></tr><tr><td>2019</td><td>$7,729</td><td>$673,000</td></tr>
    <tr class="band"><td>2020</td><td>$7,883</td><td>$687,000</td></tr><tr><td>2021</td><td>$8,041</td><td>$700,000</td></tr>
    <tr class="band"><td>2022</td><td>$8,202</td><td>$714,000</td></tr><tr><td>2023</td><td>$8,366</td><td>$729,000</td></tr>
    <tr class="band"><td>Total</td><td></td><td>$729,000</td></tr>
  </table>
  <div class="foot-line"></div><div class="brand"><i></i>northfield financial</div>
</section>
<div class="slide-num" style="left:408px;top:358px">15</div>

<section class="slide" style="left:608px;top:252px">
  <div class="title">Inflation - Cost of Living</div><div class="corner"></div><div class="rule"></div>
  <p class="copy sidebar-copy" style="left:6px;top:20px;width:46px;height:42px">Rising prices reduce buying power over time, so income needs grow each year of retirement.</p>
  <table class="table" style="left:60px;top:19px;width:50px">
    <tr class="head"><td>Year</td><td>Cost</td></tr>
    <tr><td>2014</td><td>$4,200</td></tr><tr><td>2016</td><td>$4,370</td></tr><tr><td>2018</td><td>$4,546</td></tr>
    <tr><td>2020</td><td>$4,730</td></tr><tr><td>2022</td><td>$4,921</td></tr><tr><td>2024</td><td>$5,120</td></tr>
    <tr><td>2026</td><td>$5,327</td></tr><tr><td>2028</td><td>$5,542</td></tr><tr><td>2030</td><td>$5,766</td></tr>
  </table>
  <table class="table" style="left:114px;top:19px;width:50px">
    <tr class="head"><td>Year</td><td>Cost</td></tr>
    <tr><td>2032</td><td>$5,999</td></tr><tr><td>2034</td><td>$6,241</td></tr><tr class="band"><td>2036</td><td>$6,493</td></tr>
    <tr><td>2038</td><td>$6,755</td></tr><tr><td>2040</td><td>$7,028</td></tr><tr><td>2042</td><td>$7,312</td></tr>
  </table>
  <div class="foot-line"></div><div class="brand"><i></i>northfield financial</div>
</section>
<div class="slide-num" style="left:608px;top:358px">16</div>

<section class="slide" style="left:808px;top:252px">
  <div class="title">Plan Recommendations</div><div class="corner"></div><div class="rule"></div>
  <p class="copy sidebar-copy" style="left:6px;top:20px;width:46px;height:42px">Steps we advise you take now to keep your retirement plan on track and well funded.</p>
  <div class="divider-v" style="left:56px;top:22px;height:70px"></div>
  <div class="kicker" style="left:62px;top:21px">IMMEDIATE ACTION: <span style="font-weight:400">NO LATER THAN 31 OCT</span></div>
  <div class="foot-line"></div><div class="brand"><i></i>northfield financial</div>
</section>
<div class="slide-num" style="left:808px;top:358px">17</div>

<section class="slide" style="left:1013px;top:252px">
  <div class="title">Plan Recommendations</div><div class="corner"></div><div class="rule"></div>
  <p class="copy sidebar-copy" style="left:6px;top:20px;width:46px;height:42px">Further ideas to consider as your plan matures and your needs change over the years.</p>
  <div class="divider-v" style="left:56px;top:22px;height:70px"></div>
  <div class="kicker" style="left:62px;top:21px">FOR YOUR CONSIDERATION:</div>
  <div class="foot-line"></div><div class="brand"><i></i>northfield financial</div>
</section>
<div class="slide-num" style="left:1013px;top:358px">18</div>

<!-- Row 4 -->
<section class="slide" style="left:8px;top:378px">
  <div class="title">Review &amp; Ongoing Discussion</div><div class="corner"></div><div class="rule"></div>
  <ul class="checks" style="left:30px;top:22px;width:130px">
    <li>Review Plan at Least Once a Year</li>
    <li>Monitor the Consumer Price Index (CPI) to Avoid Inflation Problems</li>
  </ul>
  <div class="foot-line"></div><div class="brand"><i></i>northfield financial</div>
</section>
<div class="slide-num" style="left:8px;top:484px">19</div>

<section class="slide" style="left:208px;top:378px">
  <div class="title">Example: Sidebar with Two Column Text</div><div class="corner"></div><div class="rule"></div>
  <p class="copy sidebar-copy" style="left:6px;top:20px;width:46px;height:60px">A short sidebar note sets the theme of this slide and leads the reader into the two columns of detail beside it.</p>
  <div class="divider-v" style="left:56px;top:22px;height:70px"></div>
  <p class="copy" style="left:62px;top:20px;width:52px;height:70px">Use this column for the main points of your discussion, written in short clear sentences that clients can follow easily during the meeting.</p>
  <p class="copy" style="left:118px;top:20px;width:52px;height:70px">Use the second column to continue the story, add examples or note the next steps agreed with the client at this review.</p>
  <div class="foot-line"></div><div class="brand"><i></i>northfield financial</div>
</section>
<div class="slide-num" style="left:208px;top:484px">20</div>

<section class="slide" style="left:408px;top:378px">
  <div class="title">Example: Three Column Text</div><div class="corner"></div><div class="rule"></div>
  <p class="copy" style="left:6px;top:20px;width:52px;height:70px">First column holds the opening ideas for this topic in a few short lines of plain text for clients.</p>
  <p class="copy" style="left:64px;top:20px;width:52px;height:70px">Second column builds on the first with more detail, figures and helpful notes on the plan.</p>
  <p class="copy" style="left:122px;top:20px;width:52px;height:70px">Third column closes the topic with a summary and the actions the client has agreed to take.</p>
  <div class="foot-line"></div><div class="brand"><i></i>northfield financial</div>
</section>
<div class="slide-num" style="left:408px;top:484px">21</div>

<section class="slide" style="left:608px;top:378px">
  <div class="title">Example: Five Vertical Text Boxes</div><div class="corner"></div><div class="rule"></div>
  <div style="position:absolute;left:6px;top:20px;width:32px;height:11px;background:var(--green)"></div>
  <div style="position:absolute;left:6px;top:34px;width:32px;height:11px;background:var(--green)"></div>
  <div style="position:absolute;left:6px;top:48px;width:32px;height:11px;background:var(--green)"></div>
  <div style="position:absolute;left:6px;top:62px;width:32px;height:11px;background:var(--green)"></div>
  <div style="position:absolute;left:6px;top:76px;width:32px;height:11px;background:var(--green)"></div>
  <p class="copy" style="left:42px;top:21px;width:130px;height:10px">A short note for the first item, with a brief line of detail.</p>
  <p class="copy" style="left:42px;top:35px;width:130px;height:10px">A short note for the second item, with a brief line of detail.</p>
  <p class="copy" style="left:42px;top:49px;width:130px;height:10px">A short note for the third item, with a brief line of detail.</p>
  <p class="copy" style="left:42px;top:63px;width:130px;height:10px">A short note for the fourth item, with a brief line of detail.</p>
  <p class="copy" style="left:42px;top:77px;width:130px;height:10px">A short note for the fifth item, with a brief line of detail.</p>
  <div class="brand"><i></i>northfield financial</div>
</section>
<div class="slide-num" style="left:608px;top:484px">22</div>

<section class="slide" style="left:808px;top:378px">
  <div class="title">Example: Six Text Boxes</div><div class="corner"></div><div class="rule"></div>
  <div class="box-head" style="left:8px;top:20px;width:50px">Lorem Ipsum</div>
  <div class="box-head" style="left:64px;top:20px;width:50px">Lorem Ipsum</div>
  <div class="box-head" style="left:120px;top:20px;width:50px">Lorem Ipsum</div>
  <p class="copy" style="left:8px;top:26px;width:50px;height:22px">Brief point for this box with one or two lines.</p>
  <p class="copy" style="left:64px;top:26px;width:50px;height:22px">Brief point for this box with one or two lines.</p>
  <p class="copy" style="left:120px;top:26px;width:50px;height:22px">Brief point for this box with one or two lines.</p>
  <div class="box-head" style="left:8px;top:55px;width:50px">Lorem Ipsum</div>
  <div class="box-head" style="left:64px;top:55px;width:50px">Lorem Ipsum</div>
  <div class="box-head" style="left:120px;top:55px;width:50px">Lorem Ipsum</div>
  <p class="copy" style="left:8px;top:61px;width:50px;height:22px">Brief point for this box with one or two lines.</p>
  <p class="copy" style="left:64px;top:61px;width:50px;height:22px">Brief point for this box with one or two lines.</p>
  <p class="copy" style="left:120px;top:61px;width:50px;height:22px">Brief point for this box with one or two lines.</p>
  <div class="foot-line"></div><div class="brand"><i></i>northfield financial</div>
</section>
<div class="slide-num" style="left:808px;top:484px">23</div>

<section class="slide" style="left:1013px;top:378px">
  <div class="photo" style="left:56px;top:0;width:124px;height:102px" role="img" aria-label="Photo of business people talking in a bright office"></div>
  <div style="position:absolute;left:10px;top:4px;width:34px;height:34px;background:var(--green)"></div>
  <div style="position:absolute;left:48px;top:20px;font-size:5px;font-weight:600;color:var(--green-dark)">northfield financial</div>
  <div style="position:absolute;left:30px;top:56px;width:150px;height:14px;background:rgba(255,255,255,.55)"></div>
  <div style="position:absolute;left:68px;top:58px;font-size:7px;color:#fff">Example: New Section</div>
</section>
<div class="slide-num" style="left:1013px;top:484px">24</div>

<!-- Row 5 -->
<section class="slide" style="left:8px;top:504px">
  <div class="title">Example: SmartArt (Large)</div><div class="corner"></div><div class="rule"></div>
  <p class="copy sidebar-copy" style="left:6px;top:20px;width:60px;height:16px">Short lead text introduces the levels of the diagram below.</p>
  <svg style="position:absolute;left:0;top:0" width="180" height="102" viewBox="0 0 180 102">
    <polygon points="62,30 74,50 50,50" fill="#2b2b2b"/>
    <polygon points="50,50 74,50 82,64 42,64" fill="#5f6062"/>
    <polygon points="42,64 82,64 90,78 34,78" fill="#3e7eb0"/>
    <polygon points="34,78 90,78 98,92 26,92" fill="var(--green-mid)"/>
    <g fill="#fff" font-size="4" text-anchor="middle"><text x="62" y="59">Text</text><text x="62" y="73">Text</text><text x="62" y="87">Text</text></g>
    <g fill="var(--green-light)"><rect x="84" y="40" width="46" height="8"/><rect x="90" y="54" width="46" height="8"/><rect x="96" y="68" width="46" height="8"/><rect x="102" y="82" width="46" height="8"/></g>
  </svg>
</section>
<div class="slide-num" style="left:8px;top:610px">25</div>

<section class="slide" style="left:208px;top:504px">
  <div class="title">Example: Sidebar with SmartArt</div><div class="corner"></div><div class="rule"></div>
  <p class="copy sidebar-copy" style="left:6px;top:20px;width:46px;height:40px">Short sidebar text explains the cycle shown in the diagram.</p>
  <svg style="position:absolute;left:0;top:0" width="180" height="102" viewBox="0 0 180 102">
    <circle cx="110" cy="62" r="22" fill="none" stroke="var(--green-light)" stroke-width="3"/>
    <circle cx="110" cy="62" r="13" fill="#3e7eb0"/>
    <text x="110" y="61" font-size="4" fill="#fff" text-anchor="middle">Lorem</text><text x="110" y="66" font-size="4" fill="#fff" text-anchor="middle">Ipsum</text>
    <g fill="var(--olive)"><circle cx="110" cy="38" r="7"/><circle cx="133" cy="55" r="7"/><circle cx="124" cy="82" r="7"/><circle cx="96" cy="82" r="7"/><circle cx="87" cy="55" r="7"/></g>
    <g font-size="2.4" fill="#fff" text-anchor="middle"><text x="110" y="39">Lorem</text><text x="133" y="56">Lorem</text><text x="124" y="83">Lorem</text><text x="96" y="83">Lorem</text><text x="87" y="56">Lorem</text></g>
  </svg>
</section>
<div class="slide-num" style="left:208px;top:610px">26</div>

<section class="slide" style="left:408px;top:504px">
  <div class="title">Example: Chart</div><div class="corner"></div><div class="rule"></div>
  <div style="position:absolute;left:0;right:0;top:19px;text-align:center;font-size:3px;color:var(--green)">Recent IPO Activity Rebounding, but Questions Remain</div>
  <div style="position:absolute;left:0;right:0;top:23px;text-align:center;font-size:2.2px;color:var(--copy)">Offers by Quarter Q1 2008 through Q1 2013</div>
  <svg style="position:absolute;left:0;top:0" width="180" height="102" viewBox="0 0 180 102">
    <line x1="30" y1="90" x2="158" y2="90" stroke="#aaa" stroke-width=".4"/>
    <g fill="var(--green-mid)">
      <rect x="36" y="84" width="7" height="6"/><rect x="50" y="86" width="7" height="4"/><rect x="64" y="82" width="7" height="8"/>
      <rect x="78" y="78" width="7" height="12"/><rect x="92" y="72" width="7" height="18"/><rect x="106" y="76" width="7" height="14"/>
      <rect x="120" y="54" width="7" height="36"/><rect x="134" y="48" width="7" height="42"/><rect x="148" y="66" width="7" height="24"/>
    </g>
    <polyline points="39,80 53,83 67,79 81,72 95,62 109,68 123,46 137,40 151,58" fill="none" stroke="#1c4f22" stroke-width=".7"/>
    <g font-size="2" fill="var(--copy)"><text x="22" y="40">$60</text><text x="22" y="65">$30</text><text x="24" y="90">$0</text></g>
  </svg>
</section>
<div class="slide-num" style="left:408px;top:610px">27</div>

<section class="slide" style="left:608px;top:504px">
  <div style="position:absolute;left:28px;top:6px;width:124px;height:52px;background:var(--olive)"></div>
  <div style="position:absolute;left:28px;width:124px;top:15px;text-align:center;color:#fff;font-size:3.4px;font-weight:700;line-height:4.4px">DANIEL R. WHITCOMBE, CFP, CLU, ChFC<br>PAUL E. WHITCOMBE, CFP</div>
  <div style="position:absolute;left:28px;width:124px;top:27px;text-align:center;color:#e2ecd5;font-size:2.2px;line-height:3px">Financial Planners<br>210 Harbour Road, Suite 4, Lakeview ON<br>Tel 555 014 2233 &nbsp; Fax 555 014 2234<br>office@northfieldfinancial.example</div>
  <div style="position:absolute;left:64px;top:70px;font-size:5px;font-weight:600;color:var(--green-dark);display:flex;align-items:center;gap:2px"><span style="width:4px;height:4px;border-radius:50%;background:var(--ink)"></span>northfield financial</div>
</section>

</main>
</body>
</html>
```